Rocket business card

Modern business card design, use of color is good with clean space too.

Things to include on card:

Quote: I add fuel to your optometry practice

- Eyewear Sales
- Admin Duties
- Revenue Collection
- Leadership
- Tech Adoption
- COGS Reduction
- Product Sourcing
-Medical Growth

Dalton Vesk, CEO
Lume Vantor
Text Me! 847-302-6194
dalton@lumevantor.net

```html
<!DOCTYPE html>
<html lang="en">
<head>
<meta charset="utf-8">
<title>Lume Vantor Business Card</title>
<link rel="stylesheet" href="https://fonts.googleapis.com/css2?family=Lato:wght@400;700&display=swap">
<style>
  :root {
    --bg: #d9d8da;
    --card: #ffffff;
    --ink: #1c1c1c;
    --orange: #f39522;
    --red: #e04d2c;
    --shadow: rgba(0,0,0,0.45);
  }
  * { margin: 0; padding: 0; box-sizing: border-box; }
  html, body { width: 1200px; height: 807px; overflow: hidden; }
  body {
    background: var(--bg);
    font-family: 'Lato', sans-serif;
    color: var(--ink);
    position: relative;
  }
  .card {
    position: absolute;
    top: 255px;
    width: 520px;
    height: 297px;
    background: var(--card);
    border-radius: 16px;
    overflow: hidden;
    box-shadow: 0 6px 18px rgba(0,0,0,0.25);
  }
  .card--front { left: 60px; }
  .card--back { left: 620px; }
  .card__waves { position: absolute; inset: 0; width: 100%; height: 100%; }
  .wave { filter: drop-shadow(0 -3px 3px var(--shadow)); }
  .wave--orange { fill: var(--orange); }
  .wave--red { fill: var(--red); }

  .brand { display: flex; align-items: center; gap: 10px; }
  .brand__dot { width: 30px; height: 30px; border-radius: 50%; background: var(--red); flex: none; }
  .brand__name { font-weight: 400; font-size: 22px; letter-spacing: 2px; text-transform: uppercase; }

  .front__contact { position: absolute; top: 24px; left: 292px; }
  .front__person { font-size: 13px; margin-top: 8px; }
  .front__line { font-size: 12px; margin-top: 6px; display: flex; align-items: center; gap: 6px; }
  .front__line svg { width: 12px; height: 12px; }

  .front__services { position: absolute; left: 26px; top: 128px; font-size: 16px; line-height: 22px; }

  .back__brand { position: absolute; top: 70px; left: 0; right: 0; justify-content: center; }
  .back__brand .brand__dot { width: 52px; height: 52px; }
  .back__brand .brand__name { font-size: 30px; letter-spacing: 3px; }
</style>
</head>
<body>
  <section class="card card--front">
    <svg class="card__waves" viewBox="0 0 520 297" aria-hidden="true">
      <path class="wave wave--orange" d="M0 248 C120 244 170 238 250 204 S400 140 520 128 L520 297 L0 297Z"/>
      <path class="wave wave--red" d="M0 268 C130 262 190 258 272 224 S420 166 520 160 L520 297 L0 297Z"/>
    </svg>
    <div class="front__contact">
      <div class="brand">
        <span class="brand__dot"></span>
        <span class="brand__name">Lume Vantor</span>
      </div>
      <p class="front__person">Dalton Vesk, CEO Lume Vantor</p>
      <p class="front__line">847-302-6194
        <svg viewBox="0 0 12 12"><circle cx="6" cy="6" r="5.5" fill="none" stroke="#1c1c1c"/><path d="M4 3h4v6H4z" fill="none" stroke="#1c1c1c"/></svg>
      </p>
      <p class="front__line">dalton@lumevantor.net
        <svg viewBox="0 0 12 12"><circle cx="6" cy="6" r="5.5" fill="none" stroke="#1c1c1c"/><path d="M3 4h6v4H3zM3 4l3 2 3-2" fill="none" stroke="#1c1c1c"/></svg>
      </p>
    </div>
    <div class="front__services">
      <p>Eyewear Sales, Admin Duties</p>
      <p>Revenue Collection, Leader Ship</p>
      <p>Tech Adoption, Cogs Reduction</p>
      <p>Product Sourcing, Medical Growth</p>
    </div>
  </section>

  <section class="card card--back">
    <svg class="card__waves" viewBox="0 0 520 297" aria-hidden="true">
      <path class="wave wave--red" d="M0 192 C90 190 120 214 190 186 S330 112 520 130 L520 297 L0 297Z"/>
      <path class="wave wave--orange" d="M0 230 C100 214 160 262 245 250 S400 182 520 190 L520 297 L0 297Z"/>
    </svg>
    <div class="brand back__brand">
      <span class="brand__dot"></span>
      <span class="brand__name">Lume Vantor</span>
    </div>
  </section>
</body>
</html>
```